Buch-/eBook-Cover für Darmtherapie für Frauen
Von Herzen Danke. Das design ist super geworden. Ich glaube ich war nicht so einfach mit meinen Änderungen. Schnelle Kommunikation. DAAANKE!!!! Ich bin so glücklich
Zielgruppe
Darmtherapie für Frauen,
Mamas und Frauen mit Kinderwunsch
Babys und Kinder
Entdecke die transformierende
Kraft der Darmtherapie!
Wie eine Darmtherapie dein Immunsystem ganzheitlich regulieren und dir bei hormonellem Ungleichgewicht helfen kann, ohne deinen Körper durch einen vermeidbaren Ärztemarathon zusätzlich zu belasten.
Ich begleite dich auf deinem Weg in ein erfülltes (Mama) – Leben.
Weil ganzheitliche Gesundheit im Darm beginnt.
Ich möchte nicht, dass dieses Buch ein weiteres ist, das du liest und dann wieder vergisst. Dieses Buch soll dich durch deine verschiedenen Lebensphasen begleiten. Du kannst dir die Informationen und Werkzeuge herausnehmen, die zu deiner Situation und deiner Familie passen.
In diesem Buch findest du freie Felder, leere Seiten und Aufgaben, in denen du deine Gedanken und Notizen festhalten kannst. Hier findest du auch Zitate, Rezepte, Übungen und Anleitungen, die speziell auf deine Lebensphase und die deiner Kinder zugeschnitten sind.
Aufgabenstellung
Eyecather Titel. Eyecather Cover. Eilt nicht Cover mit einem Heilstein oder so. Evtl Titel des Flyers mit einarbeiten: Entdecke die transformierende Kraft der Darmtherapie ( nur Vorschlag)
Es soll nicht der Flyer als Cover werden. Flyer dient nur der Firmen Farben etc
Richtiger eye Catcher Titel. Gern etwas provokativ

```html
<!DOCTYPE html>
<html lang="de">
<head>
<meta charset="utf-8">
<title>Rundum gesund mit Darmpflege – Buchcover</title>
<link rel="stylesheet" href="https://fonts.googleapis.com/css2?family=Bebas+Neue&family=Fira+Sans:wght@300;400;500&display=swap">
<style>
  :root{
    --backdrop:#d9d9d9;
    --teal:#7fbcc3;
    --leaf:#6fb2b8;
    --white:#ffffff;
    --title-shadow:#8a8f92;
    --lime:#c9c43e;
    --ink:#1e5a5c;
    --photo-skin:#a9714f;
    --photo-green:#8fa35e;
    --photo-grey:#8d8d8d;
  }
  *{margin:0;padding:0;box-sizing:border-box}
  html,body{width:1200px;height:1034px;overflow:hidden;background:var(--backdrop)}
  .cover{
    position:absolute;left:282px;top:39px;width:637px;height:956px;
    background:var(--white);overflow:hidden;
    box-shadow:10px 10px 14px rgba(0,0,0,.35);
  }
  .cover__top{
    position:absolute;left:0;top:0;width:100%;height:399px;background:var(--teal);
  }
  .cover__leaf{
    position:absolute;left:0;top:20px;width:150px;height:240px;
    background:radial-gradient(ellipse at 40% 40%, var(--leaf) 0%, rgba(111,178,184,0) 70%);
    opacity:.8;
  }
  .cover__author{
    position:absolute;left:0;right:0;top:38px;text-align:center;
    font-family:"Fira Sans",sans-serif;font-weight:400;font-size:27px;
    color:var(--white);letter-spacing:.3px;
  }
  .title{position:absolute;left:0;top:0;width:637px;height:399px}
  .title__main{
    font-family:"Bebas Neue",sans-serif;font-size:104px;fill:var(--white);
  }
  .title__shadow{
    font-family:"Bebas Neue",sans-serif;font-size:104px;fill:var(--title-shadow);
  }
  .title__mit{
    font-family:"Fira Sans",sans-serif;font-weight:300;font-size:48px;fill:var(--white);
  }
  .cover__photo{
    position:absolute;left:0;top:405px;width:100%;height:551px;
    background:
      radial-gradient(ellipse 45% 55% at 50% 30%, var(--photo-skin) 0%, rgba(169,113,79,0) 80%),
      linear-gradient(180deg, rgba(141,141,141,0) 55%, var(--photo-grey) 75%),
      linear-gradient(90deg, var(--photo-green), #b8b48a 50%, var(--photo-green));
  }
  .cover__band{position:absolute;left:0;top:0;width:637px;height:956px}
  .brand{
    position:absolute;left:23px;top:793px;width:98px;height:98px;border-radius:50%;
    background:var(--white);display:flex;align-items:center;justify-content:center;
    font-family:"Fira Sans",sans-serif;font-weight:400;font-size:15px;color:var(--teal);
  }
  .cover__audience{
    position:absolute;right:29px;top:831px;text-align:right;
    font-family:"Fira Sans",sans-serif;font-weight:400;font-size:23px;line-height:30px;color:var(--ink);
  }
</style>
</head>
<body>
  <div class="cover">
    <div class="cover__top">
      <div class="cover__leaf" role="img" aria-label="Dezentes Palmblatt-Motiv"></div>
      <div class="cover__author">Lena Vossberg</div>
      <h1>
        <svg class="title" viewBox="0 0 637 399" aria-label="Rundum gesund mit Darmpflege">
          <text class="title__shadow" x="42" y="210" textLength="558" lengthAdjust="spacingAndGlyphs">RUNDUM GESUND</text>
          <text class="title__main" x="39" y="207" textLength="558" lengthAdjust="spacingAndGlyphs">RUNDUM GESUND</text>
          <text class="title__mit" x="54" y="270">mit</text>
          <text class="title__shadow" x="139" y="324" textLength="449" lengthAdjust="spacingAndGlyphs">DARMPFLEGE</text>
          <text class="title__main" x="136" y="321" textLength="449" lengthAdjust="spacingAndGlyphs">DARMPFLEGE</text>
        </svg>
      </h1>
    </div>
    <div class="cover__photo" role="img" aria-label="Foto: Frau in grauer Sportkleidung formt mit den Händen ein Herz auf dem Bauch, grüner Hintergrund"></div>
    <svg class="cover__band" viewBox="0 0 637 956" aria-hidden="true">
      <polygon points="0,853 637,744 637,956 0,956" fill="#ffffff"/>
      <polygon points="0,861 637,752 637,956 0,956" fill="#c9c43e"/>
    </svg>
    <div class="brand">Vossberg</div>
    <p class="cover__audience">Ein Begleiter für Frauen,<br>Mamas und Paare mit Kinderwunsch<br>sowie Babys und Kinder</p>
  </div>
</body>
</html>
```